VORLEN Website Design

We need a website designed for our company VORLEN. We are a luxury lifestyle club that will provide benefits and services for our members. The site should be clean & sleek, preferably using black and white (or darker colors). (example sites: brimvale.example, tusko.example)

Here is a link of a sample page I did using wix. (https://pelmundry4.sitebuild.example/mypage) This can be used to get a general idea.

Target Market(s)

Upper Middle Class in the United States

Number of Pages Required

5+ page

Font styles to use
Sans Serif
Other font styles liked:
• Arial (or other similar fonts)

Requirements
Must have
• A clean design that is eye-catching and speaks to our company.
Nice to have
• Ideas for copy.

```html
<!DOCTYPE html>
<html lang="en">
<head>
<meta charset="utf-8">
<title>VORLEN – A Members Only Lifestyle Club</title>
<link rel="stylesheet" href="https://fonts.googleapis.com/css2?family=Montserrat:wght@400;500;600;700&family=Roboto:wght@400;500;700&display=swap">
<style>
:root{
  --accent:#1fc3ef;
  --ink:#333333;
  --muted:#6b6b6b;
  --nav:#1d1d1d;
  --dark:#3b3b3b;
  --footer:#222222;
  --light:#f5f5f5;
  --white:#ffffff;
}
*{margin:0;padding:0;box-sizing:border-box}
html,body{width:1200px;height:3586px;overflow:hidden;background:var(--white)}
body{font-family:"Roboto",Arial,sans-serif;color:var(--ink)}
.page{position:relative;width:1200px;height:3586px;overflow:hidden}
.abs{position:absolute}
.heading{font-family:"Montserrat",Arial,sans-serif;font-weight:700}
.btn{position:absolute;display:flex;align-items:center;justify-content:center;background:var(--accent);color:var(--white);font-family:"Montserrat",Arial,sans-serif;font-weight:600;font-size:12px;letter-spacing:.5px;text-transform:uppercase}
.btn-outline{background:var(--white);color:var(--accent);border:2px solid var(--accent)}

/* nav */
.nav{left:0;top:0;width:1200px;height:53px;background:var(--nav)}
.logo{font-family:"Montserrat",Arial,sans-serif;font-weight:500;color:var(--white)}
.nav .logo{left:131px;top:11px;font-size:26px}
.nav-links{left:520px;top:18px;display:flex;gap:24px;font-size:13px;color:var(--white)}
.nav-links .active{color:var(--accent)}
.nav-phone{left:852px;top:17px;display:flex;align-items:center;gap:8px;color:var(--white);font-weight:700;font-size:13px}

/* hero */
.hero-left{left:0;top:53px;width:600px;height:513px;background:linear-gradient(120deg,#6a5a52,#2f2b2c 60%,#403a3a)}
.hero-right{left:600px;top:53px;width:600px;height:444px;background:linear-gradient(135deg,#2a3b55,#8a6a5c 45%,#3c2a2a 80%)}
.hero-kicker{left:131px;top:330px;color:var(--white);font-size:28px}
.hero-title{left:131px;top:368px;width:440px;color:var(--white);font-size:38px;line-height:46px;letter-spacing:1px}
.hero-call{left:0;top:497px;width:600px;height:69px;background:rgba(110,110,110,.75);color:var(--white);font-size:19px;padding:22px 0 0 131px;font-family:"Montserrat",Arial,sans-serif}
.hero-call b{font-weight:700}
.hero-apply{left:600px;top:497px;width:600px;height:69px;background:var(--white);display:flex;align-items:center;padding-left:38px;gap:10px;font-size:12px;color:var(--ink)}

/* about */
.about-title{left:131px;top:636px;font-size:34px;color:var(--ink)}
.about-text{left:131px;width:430px;font-size:14px;line-height:22px;color:var(--muted)}
.about-frame{left:602px;top:629px;width:438px;height:315px;border:6px solid #e3e3e3}
.about-photo{left:650px;top:674px;width:438px;height:335px;background:linear-gradient(160deg,#d0509a,#8a2a70 40%,#2a1a30 85%);z-index:3}

/* services */
.services{left:0;top:956px;width:1200px;height:664px;background:radial-gradient(ellipse at 50% 40%,#4a4a4a,#333 80%)}
.services-title{left:0;top:1050px;width:1200px;text-align:center;color:var(--white);font-size:32px}
.services-sub{left:0;top:1101px;width:1200px;text-align:center;color:var(--white);font-size:19px;letter-spacing:2px}
.benefit{width:420px;text-align:center;color:var(--white);font-size:15px;line-height:22px}
.benefit svg{display:block;margin:0 auto 14px}

/* testimonials */
.members{left:0;top:1620px;width:1200px;height:471px;background:var(--light)}
.section-title{left:0;width:1200px;text-align:center;font-size:32px;color:var(--ink)}
.pager{display:flex;gap:14px;left:574px}
.pager span{width:32px;height:32px;border-radius:50%;display:flex;align-items:center;justify-content:center}
.pager .prev{border:1px solid #c8c8c8;background:var(--white)}
.pager .next{background:var(--accent)}
.card{width:290px;background:var(--white);box-shadow:0 2px 10px rgba(0,0,0,.08);text-align:center}
.quote{height:215px;top:1810px;padding-top:25px}
.avatar{width:54px;height:54px;border-radius:50%;margin:0 auto;background:linear-gradient(135deg,#c9b7a6,#6d5a4e)}
.quote h3{font-size:16px;font-weight:500;margin:14px 0 8px}
.quote p{font-size:13px;line-height:20px;color:var(--muted);padding:0 38px}

/* gallery */
.experience{left:0;top:2091px;width:495px;height:397px;background:linear-gradient(160deg,#3cb2ef,#1f8fd8 60%,#2a7fc8)}
.exp-text{right:705px;top:2388px;text-align:right;color:var(--white)}
.exp-text small{display:block;font-size:17px;font-family:"Montserrat",Arial,sans-serif;font-weight:600}
.exp-text strong{display:block;font-size:36px;font-family:"Montserrat",Arial,sans-serif;font-weight:700;line-height:40px}
.tile{width:235px;height:199px}

/* news */
.news{height:395px;top:2680px;border:1px solid #eee;box-shadow:0 2px 10px rgba(0,0,0,.05)}
.news-photo{height:172px}
.news-date{font-size:11px;color:var(--muted);margin-top:20px}
.news h3{font-family:"Montserrat",Arial,sans-serif;font-size:14px;font-weight:600;line-height:19px;margin:8px 22px 0}
.news p{font-size:13px;line-height:20px;color:var(--muted);margin:10px 26px 0}
.news .btn{position:relative;display:inline-flex;width:96px;height:32px;margin-top:14px}

/* newsletter & footer */
.newsletter{left:0;top:3155px;width:1200px;height:155px;background:var(--nav)}
.nl-title{left:131px;top:3188px;font-size:24px;color:var(--white)}
.nl-text{left:131px;top:3228px;width:540px;font-size:13px;line-height:20px;color:#aaa}
.nl-input{left:670px;top:3212px;width:285px;height:41px;background:#3a3a3a;color:#ccc;font-size:12px;padding:13px 18px;letter-spacing:.5px}
.footer{left:0;top:3310px;width:1200px;height:276px;background:var(--footer)}
.footer .logo{left:131px;top:3340px;font-size:32px}
.foot-contact{left:131px;top:3385px;color:var(--white);font-size:13px;line-height:28px}
.foot-contact span{color:var(--accent)}
.foot-col{top:3340px;color:var(--white);font-size:13px;line-height:24px}
.foot-col h4{font-family:"Montserrat",Arial,sans-serif;color:var(--accent);font-size:15px;font-weight:600;margin-bottom:14px}
.foot-col .hl{color:var(--accent);font-weight:500}
.socials{display:flex;gap:8px}
.socials span{width:26px;height:26px;border-radius:50%;background:#8a8a8a}
.foot-rule{left:131px;top:3515px;width:937px;height:1px;background:#3a3a3a}
.copyright{left:0;top:3542px;width:1200px;text-align:center;color:#9a9a9a;font-size:12px}
</style>
</head>
<body>
<div class="page">

  <!-- navigation -->
  <header class="abs nav"></header>
  <div class="abs logo" style="left:131px;top:11px;font-size:26px">VORLEN</div>
  <nav class="abs nav-links">
    <span class="active">Home</span><span>About</span><span>Services &amp; Benefits</span><span>Contact</span>
  </nav>
  <div class="abs nav-phone">
    <svg width="14" height="14" viewBox="0 0 24 24"><path fill="#1fc3ef" d="M6.6 10.8a15 15 0 0 0 6.6 6.6l2.2-2.2c.3-.3.7-.4 1-.2 1.1.4 2.3.6 3.6.6.6 0 1 .4 1 1V20c0 .6-.4 1-1 1A17 17 0 0 1 3 4c0-.6.4-1 1-1h3.5c.6 0 1 .4 1 1 0 1.3.2 2.5.6 3.6.1.3 0 .7-.2 1z"/></svg>
    123-456-7890
  </div>
  <div class="btn" style="left:975px;top:12px;width:93px;height:28px;font-size:11px">Apply Now</div>

  <!-- hero -->
  <div class="abs hero-left" role="img" aria-label="Club members celebrating together, dimmed"></div>
  <div class="abs hero-right" role="img" aria-label="Friends raising glasses at a night club"></div>
  <div class="abs hero-kicker heading" style="font-weight:600">VORLEN</div>
  <h1 class="abs hero-title heading">A MEMBERS ONLY LIFESTYLE CLUB</h1>
  <div class="abs hero-call">Call for enquiry : <b>123-456-7890</b></div>
  <div class="abs hero-apply">
    <svg width="28" height="28" viewBox="0 0 28 28"><circle cx="14" cy="14" r="14" fill="#1fc3ef"/><path d="M8 14h11M15 10l4 4-4 4" stroke="#fff" stroke-width="2" fill="none"/></svg>
    Apply Now
  </div>

  <!-- about -->
  <h2 class="abs about-title heading">ABOUT VORLEN</h2>
  <p class="abs about-text" style="top:698px">VORLEN is a members only lifestyle club founded in order to bring the best services, experiences, and opportunities to our diverse community of members.</p>
  <p class="abs about-text" style="top:780px">Our members consist of creatives, athletes, artists, and other professionals.</p>
  <div class="btn" style="left:131px;top:843px;width:127px;height:38px">Learn More</div>
  <div class="abs about-frame"></div>
  <div class="abs about-photo" role="img" aria-label="Crowd with raised hands under pink concert lights"></div>

  <!-- services -->
  <section class="abs services" role="img" aria-label="Faded party crowd backdrop"></section>
  <h2 class="abs services-title heading" style="font-weight:600">SERVICES &amp; BENEFITS</h2>
  <div class="abs services-sub">THE ULTIMATE FULL SERVICE LIFESTYLE CLUB</div>

  <div class="abs benefit" style="left:182px;top:1160px">
    <svg width="64" height="64" viewBox="0 0 64 64" fill="none" stroke="#fff" stroke-width="2"><circle cx="32" cy="32" r="9"/><circle cx="12" cy="12" r="6"/><circle cx="52" cy="12" r="6"/><circle cx="12" cy="52" r="6"/><circle cx="52" cy="52" r="6"/><path d="M17 17l8 8M47 17l-8 8M17 47l8-8M47 47l-8-8"/></svg>
    VORLEN was formed to bring the best services, experiences, and exclusive opportunities to our members.
  </div>
  <div class="abs benefit" style="left:590px;top:1160px">
    <svg width="64" height="64" viewBox="0 0 64 64" fill="none" stroke="#fff" stroke-width="2"><path d="M32 4c3 0 4 4 4 8v14l22 12v6l-22-6v12l7 5v4l-11-3-11 3v-4l7-5V38L6 44v-6l22-12V12c0-4 1-8 4-8z"/></svg>
    With everything from private member events to private jet travel, the perks of being a VORLEN member are unmatched.
  </div>
  <div class="abs benefit" style="left:182px;top:1336px">
    <svg width="64" height="64" viewBox="0 0 64 64" fill="none" stroke="#fff" stroke-width="2"><circle cx="32" cy="24" r="16"/><path d="M32 14l3 7h7l-6 4 2 7-6-4-6 4 2-7-6-4h7z"/><path d="M22 37l-6 22 9-5 4 8 3-22M42 37l6 22-9-5-4 8-3-22"/></svg>
    Professional athletes, artists, musicians, corporate professionals: Our members come from diverse backgrounds.
  </div>
  <div class="abs benefit" style="left:590px;top:1336px">
    <svg width="64" height="64" viewBox="0 0 64 64" fill="none" stroke="#fff" stroke-width="2"><circle cx="32" cy="32" r="10"/><path d="M28 6h8l1 7 6 3 6-4 6 6-4 6 3 6 7 1v8l-7 1-3 6 4 6-6 6-6-4-6 3-1 7h-8l-1-7-6-3-6 4-6-6 4-6-3-6-7-1v-8l7-1 3-6-4-6 6-6 6 4 6-3z"/></svg>
    Comprehensive services like 24/7 concierge, accountants, attorneys, private advisers, planners, investment advisors and more.
  </div>
  <div class="btn" style="left:537px;top:1526px;width:127px;height:38px">Apply Now</div>

  <!-- member testimonials -->
  <section class="abs members"></section>
  <h2 class="abs section-title heading" style="top:1675px">MEMBER SPEAKS</h2>
  <div class="abs pager" style="top:1742px">
    <span class="prev"><svg width="12" height="12" viewBox="0 0 12 12"><path d="M8 2L4 6l4 4" stroke="#aaa" stroke-width="1.5" fill="none"/></svg></span>
    <span class="next"><svg width="12" height="12" viewBox="0 0 12 12"><path d="M4 2l4 4-4 4" stroke="#fff" stroke-width="2" fill="none"/></svg></span>
  </div>
  <article class="abs card quote" style="left:131px">
    <div class="avatar" role="img" aria-label="Member portrait"></div>
    <h3>John Smith</h3>
    <p>Phasellus tellus risus, tincidunt eu scelerisque a, blandit sed metus. Aliquam ut tristique mi. Fusce vitae dignissim enim. Nam tincidunt dictum libero sed.</p>
  </article>
  <article class="abs card quote" style="left:455px">
    <div class="avatar" role="img" aria-label="Member portrait"></div>
    <h3>Peter Hens</h3>
    <p>Phasellus tellus risus, tincidunt eu scelerisque a, blandit sed metus. Aliquam ut tristique mi. Fusce vitae dignissim enim. Nam tincidunt dictum libero sed.</p>
  </article>
  <article class="abs card quote" style="left:778px">
    <div class="avatar" role="img" aria-label="Member portrait"></div>
    <h3>Claire Pat</h3>
    <p>Phasellus tellus risus, tincidunt eu scelerisque a, blandit sed metus. Aliquam ut tristique mi. Fusce vitae dignissim enim. Nam tincidunt dictum libero sed.</p>
  </article>

  <!-- experience gallery -->
  <div class="abs experience" role="img" aria-label="Concert crowd in blue light"></div>
  <svg class="abs" style="left:396px;top:2325px" width="58" height="58" viewBox="0 0 58 58"><circle cx="29" cy="29" r="27" fill="none" stroke="#fff" stroke-width="3"/><path d="M23 17l17 12-17 12z" fill="#fff"/></svg>
  <div class="abs exp-text"><small>EXPERIENCE</small><strong>WITH VORLEN</strong></div>
  <div class="abs tile" style="left:495px;top:2091px;background:linear-gradient(160deg,#b23ad0,#4a1a6a)" role="img" aria-label="Singer on a purple lit stage"></div>
  <div class="abs tile" style="left:730px;top:2091px;background:linear-gradient(160deg,#1a2a6a,#3a5ad0 50%,#101830)" role="img" aria-label="DJ mixing console"></div>
  <div class="abs tile" style="left:965px;top:2091px;background:linear-gradient(160deg,#c05a3a,#e9b070 50%,#6a2a1a)" role="img" aria-label="Cocktail on a bar counter"></div>
  <div class="abs tile" style="left:495px;top:2290px;height:198px;background:linear-gradient(160deg,#d08a3a,#3a2a30 60%,#1a1620)" role="img" aria-label="Crowd at a lit bar"></div>
  <div class="abs tile" style="left:730px;top:2290px;height:198px;background:linear-gradient(160deg,#c03ad0,#5a1a8a 60%,#1a1030)" role="img" aria-label="Dancer under violet lights"></div>
  <div class="abs tile" style="left:965px;top:2290px;height:198px;background:linear-gradient(160deg,#1a2030,#2a8aa0 50%,#101820)" role="img" aria-label="Glowing bottles on a bar"></div>

  <!-- latest news -->
  <h2 class="abs section-title heading" style="top:2545px">LATEST NEWS</h2>
  <div class="abs pager" style="top:2611px">
    <span class="prev"><svg width="12" height="12" viewBox="0 0 12 12"><path d="M8 2L4 6l4 4" stroke="#aaa" stroke-width="1.5" fill="none"/></svg></span>
    <span class="next"><svg width="12" height="12" viewBox="0 0 12 12"><path d="M4 2l4 4-4 4" stroke="#fff" stroke-width="2" fill="none"/></svg></span>
  </div>
  <article class="abs card news" style="left:131px">
    <div class="news-photo" style="background:linear-gradient(180deg,#2a4ab0,#6a8ae0 40%,#101830)" role="img" aria-label="Concert crowd under stage lights"></div>
    <div class="news-date">July 27th, 2018</div>
    <h3>Nulla eget molestie massa eleifen velit nulla facilisiulla</h3>
    <p>Phasellus tellus risus, tincidunt eu scelerisque a, blandit sed metus. Aliquam ut tristique mi fusce vitae dignissim.</p>
    <div class="btn btn-outline">Read More</div>
  </article>
  <article class="abs card news" style="left:455px">
    <div class="news-photo" style="background:linear-gradient(180deg,#5a2ad0,#d03aa0 45%,#1a1040)" role="img" aria-label="Club stage with colourful lights"></div>
    <div class="news-date">July 27th, 2018</div>
    <h3>Nulla eget molestie massa eleifen velit nulla facilisiulla</h3>
    <p>Phasellus tellus risus, tincidunt eu scelerisque a, blandit sed metus. Aliquam ut tristique mi fusce vitae dignissim.</p>
    <div class="btn">Read More</div>
  </article>
  <article class="abs card news" style="left:778px">
    <div class="news-photo" style="background:linear-gradient(180deg,#103a3a,#2aa0a0 50%,#0a1a20)" role="img" aria-label="Dance floor in teal light"></div>
    <div class="news-date">July 27th, 2018</div>
    <h3>Nulla eget molestie massa eleifen velit nulla facilisiulla</h3>
    <p>Phasellus tellus risus, tincidunt eu scelerisque a, blandit sed metus. Aliquam ut tristique mi fusce vitae dignissim.</p>
    <div class="btn btn-outline">Read More</div>
  </article>

  <!-- newsletter -->
  <section class="abs newsletter"></section>
  <h2 class="abs nl-title heading">SUBSCRIPTION NEWSLETTER</h2>
  <p class="abs nl-text">Phasellus tellus risus, tincidunt eu scelerisque a, blandit sed metus. Aliquam ut tristique mi. Fusce vitae dignissim enim. Nam tincidunt dictum libero sed.</p>
  <div class="abs nl-input">ENTER EMAIL</div>
  <div class="btn" style="left:955px;top:3212px;width:110px;height:41px">Subscribe</div>

  <!-- footer -->
  <footer class="abs footer"></footer>
  <div class="abs logo" style="left:131px;top:3340px;font-size:32px">VORLEN</div>
  <div class="abs foot-contact">Call: <span>123-456-7890</span><br>Email: <span>info@vorlen.example</span></div>
  <div class="abs foot-col" style="left:388px">
    <h4>LINKS</h4>Home<br>About<br>Services &amp; Benefits<br>Contact
  </div>
  <div class="abs foot-col" style="left:617px">
    <h4>EVENT DATES</h4>Monday to Friday<br><span class="hl">6PM–11PM</span><br>Saturday to Sunday<br><span class="hl">9PM–01AM</span>
  </div>
  <div class="abs foot-col" style="left:840px">
    <h4>FOLLOW US</h4>
    <div class="socials"><span></span><span></span><span></span></div>
  </div>
  <div class="abs foot-rule"></div>
  <div class="abs copyright">2018 © Copyright, VORLEN, All Rights Reserved</div>

</div>
</body>
</html>
```